Cosmetic oil label design

We need a label for a cosmetic oganic Argan Oil. The oil is organic imported from Morocco, cold pressed without any preservatives. The lable is for our round 30ml Airless Bottle with clear body Matte Gold Cap, Shiny Gold Collar. We want to communicate that our product is organic natural and works for all beauty needs. We want the emphasis on the words No preservatives, additives or perfumes
We have attached a picture of the bottle and our compnay's logo.

the bottle demensions are Width/Front: 33.0mm
Length/Depth: 33.0mm
Height: 115.0mm
Lable demensions: Lenght 4inch, width 1.75inch.

let us know if you need any other information, cheers!

Target Market(s)

Our target customer is mainly women 16-70, and also men or anyone looking to have healthy skin and hair using natural products

Industry/Entity Type

Product

Requirements
Must have
• Front side must have:
- attached logo
-words: Authentic Moroccan Argan Oil, No preservatives, additives or perfumes,
L’Huile d’Argan, Produit du Maroc, Imported from Morocco, 30ml

Back side
-Ingredients: 100% Pure Argania Spinosa (Argan Oil)
-Directions: Message into skin, hair or desired area until completely absorbed
-Manufactured for and distributed by Velora Imports
417 W 92nd street New York , NY 10024
Nice to have
• Would be nice if we can fit the following information in the back of the label

Rich in vitamin E and essential fatty acids,Argan oil has several benefits. It Hydrates and nourishes skin and hair. Can be used for treating dry skin, split ends softening cuticles. It works for all types of skin.

```html
<!DOCTYPE html>
<html lang="en">
<head>
<meta charset="utf-8">
<title>Argan Oil Label – Back Panel</title>
<link href="https://fonts.googleapis.com/css2?family=Questrial&display=swap" rel="stylesheet">
<style>
  :root {
    --ink: #2b1d0d;
    --gold-deep: #4d391e;
    --gold-mid: #7d5d2d;
    --gold-warm: #c1913f;
    --gold-bright: #d5a345;
    --gold-fade: #b3883b;
    --base-deep: #463520;
  }
  html, body {
    margin: 0;
    padding: 0;
    width: 1200px;
    height: 2743px;
    overflow: hidden;
  }
  .label-back {
    position: relative;
    width: 1200px;
    height: 2743px;
    background: linear-gradient(to bottom,
      var(--gold-deep) 0%,
      var(--gold-mid) 16%,
      var(--gold-warm) 44%,
      var(--gold-bright) 62%,
      var(--gold-fade) 80%,
      var(--base-deep) 100%);
    font-family: "Questrial", "Century Gothic", sans-serif;
    color: var(--ink);
    text-align: center;
  }
  .block {
    position: absolute;
    left: 0;
    width: 100%;
    margin: 0;
    font-size: 74px;
    letter-spacing: 3px;
    white-space: nowrap;
  }
  .benefits { top: 407px; line-height: 85px; }
  .ingredients { top: 1342px; line-height: 92px; }
  .directions { top: 1686px; line-height: 88px; }
  .heading,
  .emphasis {
    -webkit-text-stroke: 1.3px var(--ink);
  }
  .heading { display: block; }
  .distributor {
    top: 2111px;
    font-size: 60px;
    line-height: 75px;
    letter-spacing: 3px;
  }
</style>
</head>
<body>
  <main class="label-back">
    <p class="block benefits">
      Rich in <span class="emphasis">vitamin E</span> and<br>
      essential fatty acids,<br>
      Argan oil has several benefits.<br>
      It hydrates and nourishes<br>
      skin and hair, can be<br>
      used for treating<br>
      dry skin, split ends<br>
      softening cuticles.<br>
      It works for<br>
      all types of skin
    </p>

    <p class="block ingredients">
      <span class="heading">Ingredients.</span>
      100% Pure Argania Spinosa<br>
      (Argan Oil)
    </p>

    <p class="block directions">
      <span class="heading">Directions</span>
      Message into<br>
      skin, hair or desired area until<br>
      completely absorbed.
    </p>

    <p class="block distributor">
      Manufactured for and distributed<br>
      by Velora Imports 417 W 92nd<br>
      street New York , NY 10024
    </p>
  </main>
</body>
</html>
```